Business Card Design for a Handbags business

We are modernising our handbags website (see attached file for new front page) and are in need of a modern business card and a related design we can use on a small marquee at the markets, on letterhead, emails etc.

As the leather handbags we mostly import are from Italy, we want a smart modern European feel to the design. We are currently thinking about changing the name of the business from Larkmoor Handbags (see www.larkmoorhandbags.com.au) to Vintessa Handbags. Also open to other suggestions you may have that communicates the European influence and quality.

Target Market(s)

25-65 year old women (and some men)

Industry/Entity Type

Business

Contact Information for Business Card

Single or double sided - whichever creates more of an impact

Font styles to use
Serif
Sans Serif

Requirements
Must have
• Clean crisp look, slightly Italian or European look and feel to reflect where the handbags are imported from
Nice to have
• open to ideas

```html
<!DOCTYPE html>
<html lang="en">
<head>
<meta charset="utf-8">
<title>Vintessa Handbags – Business Card</title>
<link rel="stylesheet" href="https://fonts.googleapis.com/css2?family=Crimson+Text&family=Tinos&display=swap">
<style>
  :root {
    --page: #ffffff;
    --card-edge: #8a8a8a;
    --stone: #d3d1c6;
    --lime: #8dc63f;
    --ink: #231f20;
    --sea-deep: #1f3a48;
    --sea-light: #3c5d6b;
    --linen: #eeeeec;
  }
  * { margin: 0; padding: 0; box-sizing: border-box; }
  html, body {
    width: 1200px;
    height: 346px;
    overflow: hidden;
    background: var(--page);
  }
  .sheet { position: relative; width: 1200px; height: 346px; }

  .side-label {
    position: absolute;
    top: 6px;
    font-family: "Crimson Text", serif;
    font-size: 15px;
    color: var(--ink);
  }
  .side-label--front { left: 14px; }
  .side-label--back { left: 616px; }

  .card {
    position: absolute;
    width: 573px;
    height: 302px;
    border: 1px solid var(--card-edge);
    overflow: hidden;
    background: var(--page);
  }
  .card--front { left: 14px; top: 32px; }
  .card--back { left: 616px; top: 30px; }

  .card__art {
    position: absolute;
    inset: 0;
    width: 100%;
    height: 100%;
  }

  .brand-band {
    position: absolute;
    left: 0; right: 0; bottom: 0;
    height: 43px;
    background: var(--lime);
  }

  .front-title {
    position: absolute;
    right: 28px;
    top: 210px;
    font-family: "Crimson Text", serif;
    font-weight: 400;
    font-size: 42px;
    line-height: 1;
    color: var(--ink);
    white-space: nowrap;
  }

  .back-details {
    position: absolute;
    left: 0; right: 0;
    top: 167px;
    text-align: center;
    color: var(--ink);
  }
  .back-details__name {
    font-family: "Crimson Text", serif;
    font-weight: 400;
    font-size: 26px;
    line-height: 28px;
    margin-bottom: 2px;
  }
  .back-details__line {
    font-family: "Tinos", serif;
    font-size: 13.5px;
    line-height: 17.5px;
    white-space: nowrap;
  }
</style>
</head>
<body>
<div class="sheet">
  <span class="side-label side-label--front">front</span>
  <span class="side-label side-label--back">back</span>

  <section class="card card--front">
    <svg class="card__art" viewBox="0 0 573 302" preserveAspectRatio="none">
      <defs>
        <linearGradient id="lifestyle-tones" x1="0" y1="0" x2="1" y2="1">
          <stop offset="0" stop-color="var(--linen)"/>
          <stop offset="0.3" stop-color="var(--sea-light)"/>
          <stop offset="0.7" stop-color="var(--sea-deep)"/>
          <stop offset="1" stop-color="var(--linen)"/>
        </linearGradient>
      </defs>
      <rect x="0" y="0" width="430" height="260" fill="url(#lifestyle-tones)"
            role="img" aria-label="Photo of a woman in white trousers carrying a red leather handbag by the sea"/>
      <polygon points="426,0 573,0 573,260 166,260" fill="var(--stone)"/>
    </svg>
    <h1 class="front-title">Vintessa Handbags</h1>
    <div class="brand-band"></div>
  </section>

  <section class="card card--back">
    <div class="back-details">
      <p class="back-details__name">Vintessa Handbags</p>
      <p class="back-details__line">58 Calloway Street, BRENDALE ACT 2914</p>
      <p class="back-details__line">Telephone: 02 61984472, Marisa: 0412 583 906</p>
      <p class="back-details__line">Tess: 0427 318640, E-mail: info@vintessahandbags.com.au</p>
    </div>
    <div class="brand-band"></div>
  </section>
</div>
</body>
</html>
```